Onboarding Infographic/brochure

We are a small criminal defense firm looking to create some sort of infographic or brochure that we can onboard new clients with. We are currently sending it out via email but want something a bit cooler and fun to send to clients. The information is:

A Few Quick Rules

We are here to help each step of the way. While questions are never discouraged, this letter will answer some of the most common ones we get asked.

Communications

As a client, you should always be in the loop. While we will try to respond to questions as quickly as possible, sometimes we are unable to respond right away. Do not worry - we promise to get back to you soon. Some questions might take some time to research, and a correct answer is better than a quick one.

Appointments

One of the benefits of having an attorney is the ability to discuss your case outside of court, minus the stress and headaches. If you need an appointment, please contact the office.

Appointments must be scheduled in advance. We do not want you to make a special trip to the office only to learn that we are in court or otherwise unavailable.

Jail Visits

If your family member is currently in jail, we take that very seriously. We will visit your loved one and introduce ourselves. While the case is ongoing, we ask that a family member be designated a “contact” person so that messages can be relayed quickly. Never discuss the facts of the case over the phone with someone who is in jail. Jail calls are recorded and we have seen too many cases go south based on remarks made over recorded lines.

Police Reports and Discovery

We will do our best to provide you with copies of everything we receive on your case. Most information will be emailed, so please keep your email address up to date.

Changes in Contact Information

If you move or change numbers during the case, please let us know. It is difficult to help if we are unable to reach you, and helping you is why we are here.

Court Appearances

Cases do not get resolved as quickly as they do on television. Expect there to be several hearings in your case and it may be necessary for you to attend one or more of them. If a hearing is set, you will receive notice of the date and time of each hearing.

Billing and Collections

We understand that this investment was a huge decision for you. As we focus on providing the best representation, we will need for you to stay on schedule with any payment arrangements agreed to at the time of your initial consultation.

Again, thank you for your trust in us. We look forward to getting a fantastic outcome on your case.

Target Market(s)

Criminal defense clients and their families

Industry/Entity Type

Legal

Font styles to use
Serif

Requirements
Must have
• Must incorporate all of the rules we email out. Would like diagrams, images or pictures
Nice to have
• We attached a Welcome brochure. Not sure I want it to look super similar, hence the request for infographic.

```html
<!DOCTYPE html>
<html lang="en">
<head>
<meta charset="utf-8">
<title>A Few Quick Rules – Client Onboarding</title>
<link href="https://fonts.googleapis.com/css2?family=Allura&family=Montserrat:wght@500;600;900&family=Open+Sans:wght@400;600;700&display=swap" rel="stylesheet">
<style>
  :root{
    --navy:#1f2a44;
    --ink:#26314d;
    --muted:#4a5570;
    --white:#ffffff;
    --paper:#ffffff;
    --body-light:#e8ebf2;
    --icon-bg:#ffffff;
  }
  *{box-sizing:border-box;margin:0;padding:0}
  html,body{width:878px;height:1200px;overflow:hidden;background:var(--paper)}
  .sheet{position:relative;width:878px;height:1200px;background:var(--paper);font-family:"Open Sans",Arial,sans-serif;color:var(--ink)}

  /* left column */
  .intro{position:absolute;left:0;top:0;width:440px;height:1200px}
  .title-few{position:absolute;left:48px;top:40px;font-family:"Allura",cursive;font-size:170px;line-height:1;color:var(--navy);transform:rotate(-6deg)}
  .title-rules{position:absolute;left:58px;top:215px;font-family:"Montserrat",Arial,sans-serif;font-weight:900;font-size:66px;line-height:.92;letter-spacing:1px;color:var(--navy)}
  .lead{position:absolute;left:58px;top:400px;width:340px;font-size:19px;line-height:1.4;color:var(--muted)}
  .lead strong{font-weight:700;color:var(--navy)}
  .hero{position:absolute;left:0;top:640px;width:440px;height:330px;background:linear-gradient(135deg,#e9ebef 0%,#bfc4cf 45%,#7a6a5a 75%,#4a3a30 100%)}
  .site-url{position:absolute;left:12px;top:1180px;transform-origin:left top;transform:rotate(-90deg);font-family:"Montserrat",Arial,sans-serif;font-weight:600;font-size:12px;letter-spacing:2px;color:var(--muted);white-space:nowrap}
  .brand{position:absolute;left:60px;top:1055px;display:flex;align-items:center;gap:14px}
  .brand-dot{width:18px;height:18px;border-radius:50%;background:var(--navy)}
  .brand-name{font-family:"Open Sans",Arial,sans-serif;font-weight:600;font-size:26px;line-height:1;color:var(--navy);white-space:nowrap}

  /* right column */
  .rules{position:absolute;left:440px;top:0;width:438px;height:1200px;background:var(--navy);padding:20px 26px 0 20px;color:var(--white)}
  .rule{display:flex;gap:14px;margin-bottom:15px}
  .rule-icon{flex:0 0 40px;width:40px;height:40px;border-radius:50%;background:var(--icon-bg);display:flex;align-items:center;justify-content:center}
  .rule-icon svg{width:22px;height:22px}
  .rule-body h2{font-family:"Montserrat",Arial,sans-serif;font-weight:500;font-size:15px;letter-spacing:.3px;text-transform:uppercase;white-space:nowrap;margin:10px 0 6px}
  .rule-body p{font-size:11.3px;line-height:1.45;margin-bottom:6px;color:var(--body-light)}
  .closing{padding-left:54px;font-size:11.3px;line-height:1.45;color:var(--body-light)}
</style>
</head>
<body>
<main class="sheet">
  <section class="intro">
    <div class="title-few">few</div>
    <h1 class="title-rules">QUICK<br>RULES</h1>
    <p class="lead">We are here to <strong>help each step</strong> of the way. While questions are never discouraged, this letter will answer some of the most common ones we get asked.</p>
    <div class="hero" role="img" aria-label="Photo of a judge's gavel resting on a desk beside legal papers"></div>
    <div class="site-url">WWW.CONCORDIALEGALGROUP.COM</div>
    <div class="brand">
      <span class="brand-dot"></span>
      <span class="brand-name">Concordia Legal Group</span>
    </div>
  </section>

  <section class="rules">
    <article class="rule">
      <div class="rule-icon"><svg viewBox="0 0 24 24" fill="#1f2a44"><path d="M3 4h18v12H9l-5 4v-4H3z"/></svg></div>
      <div class="rule-body"><h2>Communications</h2>
      <p>As a client, you should always be in the loop. While we will try to respond to questions as quickly as possible, sometimes we are unable to respond right away. Do not worry – we promise to get back to you soon. Some questions might take some time to research, and a correct answer is better than a quick one.</p></div>
    </article>
    <article class="rule">
      <div class="rule-icon"><svg viewBox="0 0 24 24" fill="#1f2a44"><path d="M3 5h18v16H3z" fill="none" stroke="#1f2a44" stroke-width="2"/><rect x="3" y="5" width="18" height="5"/><rect x="7" y="2" width="2" height="5"/><rect x="15" y="2" width="2" height="5"/></svg></div>
      <div class="rule-body"><h2>Appointments</h2>
      <p>One of the benefits of having an attorney is the ability to discuss your case outside of court, minus the stress and headaches. If you need an appointment, please contact the office.</p>
      <p>Appointments must be scheduled in advance. We do not want you to make a special trip to the office only to learn that we are in court or otherwise unavailable.</p></div>
    </article>
    <article class="rule">
      <div class="rule-icon"><svg viewBox="0 0 24 24" fill="#1f2a44"><rect x="3" y="3" width="18" height="2"/><rect x="3" y="19" width="18" height="2"/><rect x="5" y="5" width="2" height="14"/><rect x="9" y="5" width="2" height="14"/><rect x="13" y="5" width="2" height="14"/><rect x="17" y="5" width="2" height="14"/></svg></div>
      <div class="rule-body"><h2>Jail Visits</h2>
      <p>If your family member is currently in jail, we take that very seriously. We will visit your loved one and introduce ourselves. While the case is ongoing, we ask that a family member be designated a “contact” person so that messages can be relayed quickly. Never discuss the facts of the case over the phone with someone who is in jail. Jail calls are recorded and we have seen too many cases go south based on remarks made over recorded lines.</p></div>
    </article>
    <article class="rule">
      <div class="rule-icon"><svg viewBox="0 0 24 24" fill="#1f2a44"><path d="M12 2l2.9 6.3 6.9.7-5.2 4.6 1.5 6.8L12 17l-6.1 3.4 1.5-6.8L2.2 9l6.9-.7z"/></svg></div>
      <div class="rule-body"><h2>Police Reports and Discovery</h2>
      <p>We will do our best to provide you with copies of everything we receive on your case. Most information will be emailed, so please keep your email address up to date.</p></div>
    </article>
    <article class="rule">
      <div class="rule-icon"><svg viewBox="0 0 24 24" fill="#1f2a44"><rect x="2" y="5" width="20" height="14" rx="2" fill="none" stroke="#1f2a44" stroke-width="2"/><circle cx="8" cy="11" r="2.5"/><path d="M4 17c.5-2.5 2-3.5 4-3.5s3.5 1 4 3.5z"/><rect x="14" y="9" width="5" height="1.8"/><rect x="14" y="13" width="5" height="1.8"/></svg></div>
      <div class="rule-body"><h2>Changes in Contact Information</h2>
      <p>If you move or change numbers during the case, please let us know. It is difficult to help if we are unable to reach you, and helping you is why we are here.</p></div>
    </article>
    <article class="rule">
      <div class="rule-icon"><svg viewBox="0 0 24 24" fill="#1f2a44"><path d="M12 2l10 5H2z"/><rect x="4" y="9" width="2.5" height="9"/><rect x="9" y="9" width="2.5" height="9"/><rect x="13.5" y="9" width="2.5" height="9"/><rect x="17.5" y="9" width="2.5" height="9"/><rect x="2" y="19" width="20" height="3"/></svg></div>
      <div class="rule-body"><h2>Court Appearances</h2>
      <p>Cases do not get resolved as quickly as they do on television. Expect there to be several hearings in your case and it may be necessary for you to attend one or more of them. If a hearing is set, you will receive notice of the date and time of each hearing.</p></div>
    </article>
    <article class="rule">
      <div class="rule-icon"><svg viewBox="0 0 24 24"><text x="12" y="19" text-anchor="middle" font-family="Montserrat, Arial, sans-serif" font-weight="600" font-size="19" fill="#1f2a44">$</text></svg></div>
      <div class="rule-body"><h2>Billing and Collections</h2>
      <p>We understand that this investment was a huge decision for you. As we focus on providing the best representation, we will need for you to stay on schedule with any payment arrangements agreed to at the time of your initial consultation.</p></div>
    </article>
    <p class="closing">Again, thank you for your trust in us. We look forward to getting a fantastic outcome on your case.</p>
  </section>
</main>
</body>
</html>
```